Create a packaging design for a new deodorant

New product container label. The jar is 2.75" in diameter and 2.75" high. The (transparent) label size is 1.5" by 8.5" and will wrap nearly fully around the jar when applied. Approximately 3.25" of the label will be devoted to the name and front section of the jar (what I am requesting you to design). Remaining part of the label will include a brief description, directions, general warning, ingredients, manufacturer, distributor, and barcode. The deodorant name is TOV. It is a clear colorless solution, ecologically friendly, naturally occurring deodorant salt solution. Water based, no alcohol, non-sticky, non-waxy, non-staining, just simple, clean and effective. Nature's way of getting the job done. Label to use transparent green and/or blue colors. Phrases such as " Fresh as a Springtime shower" or "Fresh as an ocean breeze" might be used. The deodorant has a NEW, unique, revolutionary applicator.

Target Market(s)

All adult men and women

Industry/Entity Type

Product

Number of Pages Required

1 page

Requirements
Nice to have
• TOV
• This is a new deodorant, a simple but elegant solution to an age-old problem.
• Why I Hate Deodorants
• I’ve had my share of problems with deodorants, and with antiperspirants for that matter, too. First off, the last thing I want to do when I step out of the shower is to put some sticky, slimy, or waxy goop on clean skin. I don’t like it when it feels like skin sticks together in skin folds. When I used to use the old stick deodorants, I would periodically scrape the edge of the plastic container against my skin and cause an abrasion that would then be irritated for the next 3 days. This would be particularly true when I got down to the bottom of the stick and the medication surface flattened out in the dispenser. Sometimes the deodorant or antiperspirant itself would cause such abrasions to grow red and angry and force me to stop using it altogether for the next week. Then I’d be hunting (and hurting) for alternatives. So every few months I would spend lots of time in the store looking at all the different brands of deodorants to find something that was a bit different - less caustic, less sticky, less stinky, or in a different dispenser that might work better for me. Roll-on deodorants work for me until they don’t. Half the time I’m trying to hold the bottle upside down and squeezing it so the product comes out. The other half of the time the roller ball gets stuck and I’m trying to get it to turn. What a waste of time. Or if it pours out, I have to spread it all over the place to get it thin enough to dry out. I dispensed with antiperspirants years ago when I had to throw away some of my favorite shirts because of sweat (really antiperspirant chemical) stains. I’ve also seen enough people with hidradenitis (infected sweat glands from using some antiperspirants) to know that some of these products that clog skin pores can be serious skin irritants.
• I’m a Natural Kind of Guy
• Don’t get me wrong. I’m not a tree hugger. I haven’t been out on the high seas in a rowboat maneuvering between a harpooner and a whale. But by the same token I don’t buy 3-step hair treatments. I don’t color my hair either. I don’t lounge around in bubble baths. And I don’t like to use heavy-scented cleansers, shampoos or skin products. I’m just looking for something clean, plain and simple ...something that works, that’s safe and dependable. Maybe even a natural product that has a long track record of safety and effectiveness.
• Just try it.....(There’s nothing more we’ll need to say!!)
• TOV uses a natural mineral salt, water, and a preservative. Nothing more. TOV has a unique and patented dispenser. The dispenser was made for the product and made for the job. One swipe application and you’re done! YOU can control the amount of deodorant applied by the sponge applicator. TOV is WATER-BASED. NO ALCOHOL. NO CHEMICALS. NO IRRITANTS. It dries quickly. No drips like you can get from spray bottles. The applicator doesn’t clog up or stop rolling. And it NEVER stains clothing. It’s just simple...easy...effective. And with a simple product we don’t have to charge a lot of money for it. So it’s inexpensive, too. I know you’re going to like this product.
• Swipe it on.... Odor gone!

```html
<!DOCTYPE html>
<html lang="en">
<head>
<meta charset="utf-8">
<title>TOV Deodorant – Front Label</title>
<link rel="stylesheet" href="https://fonts.googleapis.com/css2?family=Open+Sans:wght@600;700&display=swap">
<style>
  :root {
    --canvas-bg: #ffffff;
    --label-silver-light: #e4e4e4;
    --label-silver-mid: #c9c9c9;
    --label-silver-dark: #a9a9a9;
    --panel-edge: #0a6fb9;
    --panel-mid: #1b93cc;
    --panel-glow: #38b6c9;
    --brand-silver: #eceff1;
    --tagline: #ffffff;
    --claims: #444444;
  }
  * { margin: 0; padding: 0; box-sizing: border-box; }
  html, body {
    width: 1200px;
    height: 862px;
    overflow: hidden;
    background: var(--canvas-bg);
  }
  .canvas {
    position: relative;
    width: 1200px;
    height: 862px;
    font-family: "Open Sans", Arial, sans-serif;
  }
  .front-label {
    position: absolute;
    left: 144px;
    top: 184px;
    width: 912px;
    height: 494px;
    border-radius: 14px;
    background: linear-gradient(90deg,
      var(--label-silver-dark) 0%,
      var(--label-silver-light) 22%,
      var(--label-silver-mid) 45%,
      var(--label-silver-light) 62%,
      var(--label-silver-dark) 80%,
      var(--label-silver-light) 94%,
      var(--label-silver-mid) 100%);
  }
  .brand-panel {
    position: absolute;
    left: 53px;
    top: 53px;
    width: 806px;
    height: 296px;
    border-radius: 16px;
    background: radial-gradient(ellipse 60% 85% at 50% 45%,
      var(--panel-glow) 0%, var(--panel-mid) 55%, var(--panel-edge) 100%);
    display: flex;
    flex-direction: column;
    align-items: center;
  }
  .brand-name {
    margin-top: 22px;
    font-weight: 700;
    font-size: 180px;
    line-height: 180px;
    letter-spacing: 100px;
    padding-left: 100px;
    color: var(--brand-silver);
  }
  .tagline {
    margin-top: 8px;
    font-weight: 700;
    font-size: 40px;
    line-height: 48px;
    letter-spacing: 0.5px;
    color: var(--tagline);
  }
  .claims {
    position: absolute;
    left: 0;
    top: 366px;
    width: 912px;
    text-align: center;
    font-weight: 700;
    font-size: 23px;
    line-height: 44px;
    letter-spacing: 0.4px;
    color: var(--claims);
  }
</style>
</head>
<body>
  <main class="canvas">
    <section class="front-label">
      <div class="brand-panel">
        <h1 class="brand-name">TOV</h1>
        <p class="tagline">FRESH AS AN OCEAN BREEZE</p>
      </div>
      <p class="claims">WATER-BASED. NO ALCOHOL. NO CHEMICALS. NO IRRITANTS</p>
    </section>
  </main>
</body>
</html>
```